Etiketten-Design für neue Biermarke
Zielgruppe
Es soll eine neue Biermarke entwickelt werden. Die drei grundlegenden Sorten sind: Pils, Radler, Helles. Für die neue Biermarke soll ein Markenname, ein Logo und ein Etikettendesign gestaltet werden. Das Bier soll traditionell sein und den typischen Biertrinker ansprechen. Die Zielgruppe der Biermarke ist die breite Masse. Das Bier soll für 9,90€ verkauft werden.
Aufgabenstellung
Das Design der Etiketten sollte klassisch und traditionell wirken. Es dürfen gerne klassische, historische und urige Elemente wie Hopfen, Bierfass, altertümliche Illustrationen, etc. verwendet werden. Das Bier sollte weder in Richtung eines Craft Bieres noch in die Richtung eines jungen/hippen Bieres gehen.

```html
<!DOCTYPE html>
<html lang="de">
<head>
<meta charset="utf-8">
<title>Alt-Hainer Helles – Etikett</title>
<link rel="stylesheet" href="https://fonts.googleapis.com/css2?family=Abril+Fatface&family=Pacifico&family=Playfair+Display:wght@500;700&display=swap">
<style>
  :root {
    --paper: #ffffff;
    --ink-brown: #371910;
    --ribbon-red: #a62923;
    --ribbon-dark: #7e1b17;
    --gold-light: #d8c896;
    --gold-mid: #b9a36f;
    --gold-deep: #9a8452;
    --hop-tan: #b68e58;
  }
  html, body {
    margin: 0;
    padding: 0;
    width: 1200px;
    height: 1181px;
    overflow: hidden;
    background: var(--paper);
  }
  .label {
    display: block;
    width: 1200px;
    height: 1181px;
  }
  .ring-text {
    font-family: "Playfair Display", serif;
    font-weight: 700;
    font-size: 25px;
    letter-spacing: 4px;
    fill: var(--ink-brown);
  }
  .variety-name {
    font-family: "Pacifico", cursive;
    font-size: 66px;
    fill: var(--paper);
  }
  .year {
    font-family: "Playfair Display", serif;
    font-weight: 500;
    font-size: 78px;
    fill: var(--ink-brown);
  }
  .brand-name {
    font-family: "Abril Fatface", serif;
    font-size: 190px;
    fill: var(--ink-brown);
  }
  .beer-style {
    font-family: "Abril Fatface", serif;
    font-size: 132px;
    fill: var(--ink-brown);
  }
</style>
</head>
<body>
<svg class="label" viewBox="0 0 1384 1362" xmlns="http://www.w3.org/2000/svg">
  <defs>
    <linearGradient id="gold-frame" x1="0" y1="0" x2="1" y2="1">
      <stop offset="0" stop-color="var(--gold-deep)"/>
      <stop offset="0.4" stop-color="var(--gold-light)"/>
      <stop offset="0.75" stop-color="var(--gold-mid)"/>
      <stop offset="1" stop-color="var(--gold-deep)"/>
    </linearGradient>
    <radialGradient id="scene-tone" cx="0.5" cy="0.6" r="0.6">
      <stop offset="0" stop-color="#6a4632"/>
      <stop offset="1" stop-color="#e9e1db"/>
    </radialGradient>
    <path id="ring-path" d="M 215 680 A 437 540 0 1 1 1089 680 A 437 540 0 1 1 215 680 Z"/>
    <path id="style-arc" d="M 425 1000 Q 650 1180 880 1000"/>
  </defs>

  <!-- frame -->
  <g class="oval-frame">
    <ellipse cx="652" cy="680" rx="527" ry="655" fill="url(#gold-frame)"/>
    <ellipse cx="652" cy="680" rx="507" ry="635" fill="var(--paper)"/>
    <ellipse cx="652" cy="680" rx="498" ry="626" fill="none" stroke="url(#gold-frame)" stroke-width="5"/>
  </g>

  <!-- circular claim -->
  <text class="ring-text">
    <textPath href="#ring-path" startOffset="170" textLength="1195" lengthAdjust="spacing">NACH DEUTSCHER BRAUQUALITÄT · PREMIUM PILS · GARANTIERT BESTE ROHSTOFFE</textPath>
  </text>
  <text class="ring-text">
    <textPath href="#ring-path" startOffset="1705" textLength="1195" lengthAdjust="spacing">NACH DEUTSCHER BRAUQUALITÄT · PREMIUM PILS · GARANTIERT BESTE ROHSTOFFE</textPath>
  </text>

  <!-- illustration area -->
  <rect x="435" y="370" width="412" height="285" rx="40" fill="url(#scene-tone)" opacity="0.55"
        role="img" aria-label="Illustration: Holzfass vor Tannenwald mit Vögeln"/>

  <!-- ribbon -->
  <g class="ribbon">
    <polygon points="380,292 470,282 468,385 383,402 412,348" fill="var(--ribbon-dark)"/>
    <polygon points="835,282 922,292 893,348 920,402 837,385" fill="var(--ribbon-dark)"/>
    <path d="M 422 256 Q 650 228 880 256 L 876 360 Q 650 336 428 360 Z" fill="var(--ribbon-red)"/>
    <text class="variety-name" x="655" y="330" text-anchor="middle">Helles</text>
  </g>

  <!-- founding year -->
  <text class="year" x="233" y="627" text-anchor="middle">18</text>
  <text class="year" x="1066" y="627" text-anchor="middle">97</text>

  <!-- brand -->
  <text class="brand-name" x="668" y="826" text-anchor="middle" textLength="770" lengthAdjust="spacingAndGlyphs">ALT-HAINER</text>

  <!-- hops -->
  <g class="hops" role="img" aria-label="Illustration: drei Hopfendolden">
    <ellipse cx="564" cy="902" rx="30" ry="33" fill="var(--hop-tan)"/>
    <ellipse cx="645" cy="945" rx="28" ry="35" fill="var(--hop-tan)"/>
    <ellipse cx="726" cy="902" rx="30" ry="33" fill="var(--hop-tan)"/>
  </g>

  <!-- beer style -->
  <text class="beer-style" text-anchor="middle">
    <textPath href="#style-arc" startOffset="50%" textLength="440" lengthAdjust="spacingAndGlyphs">PILSNER</textPath>
  </text>
</svg>
</body>
</html>
```